Varneck Law Business cards and stationary design project

We are looking for a stationary design for business cards (double sided), 8x10, 5x7, and legal and standard envelopes.

We would like the design to match the logo that we have already.
Color palate preferred is Teal, White, grey and any others that will look good for a professional law firm.

We would like this statement: "RELATIONSHIPS. RESPECT. RESULT" to be on the back of the business cards and maybe on the stationary if it looks good.

Please see link to website for more information: www.varneck-law-example.com

Target Market(s)

Potential clients that need Attorney services.

Industry/Entity Type

Law Firm

Contact Information for Business Card

We would like the front and back to be two different colors. Current business cards are teal front, grey back and are a vertical design. We are open to options with colors.

Font styles to use
Serif

Colors
33a6d7
33b8a4
b9b9b9
5c5c5c

Requirements
Must have
• Logo supplied needs to go on the card and stationary.
• Match website color palate, www.varneck-law-example.com
• Be professional and not too wordy.
• Criminal Law, Civil Litigation, Personal Injury, Restraining Orders need to be on the card.
Nice to have
• RELATIONSHIPS. RESPECT. RESULTS. on the back of the card.
Should not have
• Not be too busy/wordy or too flashy.

```html
<!DOCTYPE html>
<html lang="en">
<head>
<meta charset="utf-8">
<title>Varneck Law – Business Card</title>
<link rel="stylesheet" href="https://fonts.googleapis.com/css2?family=Jost:wght@400;500&display=swap">
<style>
  :root {
    --teal: #33b8a4;
    --teal-deep: #22909a;
    --grey-dark: #5c5c5c;
    --grey-light: #b9b9b9;
    --ink: #4a4a4a;
    --white: #ffffff;
    --stage: #ecebe8;
  }
  * { box-sizing: border-box; margin: 0; padding: 0; }
  html, body { width: 1200px; height: 1200px; overflow: hidden; }
  body {
    background: var(--stage);
    font-family: "Jost", "Futura", sans-serif;
    display: flex;
    flex-direction: column;
    align-items: center;
    justify-content: center;
    gap: 60px;
  }
  .card {
    position: relative;
    width: 860px;
    height: 491px;
    overflow: hidden;
    box-shadow: 0 6px 18px rgba(0,0,0,0.18);
  }

  .brand {
    position: absolute;
    display: flex;
    flex-direction: column;
    align-items: center;
    font-family: "Jost", "Futura", sans-serif;
    font-weight: 400;
    white-space: nowrap;
  }
  .brand__mark { border-radius: 50%; }

  /* Back side */
  .card--back { background: var(--grey-dark); }
  .card--back .brand {
    top: 110px;
    left: 0; right: 0;
    gap: 22px;
    color: var(--white);
    font-size: 48px;
    letter-spacing: 2px;
  }
  .card--back .brand__mark {
    width: 76px; height: 76px;
    background: var(--white);
  }
  .tagline-band {
    position: absolute;
    left: 0; right: 0;
    top: 366px;
    height: 46px;
    background: var(--grey-light);
    display: flex;
    align-items: center;
    justify-content: center;
    font-size: 21px;
    letter-spacing: 5px;
    color: var(--teal);
    text-transform: uppercase;
  }

  /* Front side */
  .card--front { background: var(--white); }
  .accent-square {
    position: absolute;
    top: 0;
    left: 82px;
    width: 220px;
    height: 168px;
    background: var(--teal);
  }
  .card--front .brand {
    top: 186px;
    left: 60px;
    width: 270px;
    gap: 14px;
    color: var(--teal-deep);
    font-size: 32px;
    letter-spacing: 1px;
  }
  .card--front .brand__mark {
    width: 52px; height: 52px;
    background: var(--teal-deep);
  }
  .contact {
    position: absolute;
    top: 58px;
    left: 430px;
    color: var(--ink);
    font-size: 19px;
    line-height: 1.3;
  }
  .contact__name { color: var(--teal); font-weight: 500; font-size: 20px; }
  .contact__role { margin-bottom: 16px; }
  .contact__list { list-style: none; margin-bottom: 16px; }
  .contact__list li { display: flex; align-items: center; gap: 10px; }
  .contact__list svg { width: 16px; height: 16px; flex: none; }
  .contact__address { font-style: normal; }
  .practice-band {
    position: absolute;
    left: 0; right: 0; bottom: 0;
    height: 96px;
    background: var(--teal);
    color: var(--white);
    font-size: 20px;
    letter-spacing: 1.5px;
    display: flex;
    align-items: center;
    padding-left: 48px;
  }
</style>
</head>
<body>

  <section class="card card--back" aria-label="Business card back">
    <div class="brand">
      <span class="brand__mark" aria-hidden="true"></span>
      <span class="brand__name">Varneck Law</span>
    </div>
    <div class="tagline-band">Relationships. Respect. Result</div>
  </section>

  <section class="card card--front" aria-label="Business card front">
    <div class="accent-square"></div>
    <div class="brand">
      <span class="brand__mark" aria-hidden="true"></span>
      <span class="brand__name">Varneck Law</span>
    </div>

    <div class="contact">
      <p class="contact__name">Dana Varneck</p>
      <p class="contact__role">trial lawyer</p>
      <ul class="contact__list">
        <li>
          <svg viewBox="0 0 16 16" aria-hidden="true"><path fill="var(--teal)" d="M3.5 1.5l2.3 2.7-1.3 1.6c.9 2 2.4 3.5 4.4 4.4l1.6-1.3 2.7 2.3-1.4 2.1C6.7 13 3 9.3 1.4 2.9z"/></svg>
          (555) 014-2290
        </li>
        <li>
          <svg viewBox="0 0 16 16" aria-hidden="true"><rect x="1" y="3" width="14" height="10" fill="var(--teal)"/><path d="M1.5 3.5L8 9l6.5-5.5" stroke="#fff" stroke-width="1.3" fill="none"/></svg>
          dana@varneck-law-example.com
        </li>
        <li>
          <svg viewBox="0 0 16 16" aria-hidden="true"><circle cx="8" cy="8" r="6.5" fill="var(--teal)"/><path d="M1.5 8h13M8 1.5c-3 3.5-3 9.5 0 13M8 1.5c3 3.5 3 9.5 0 13" stroke="#fff" stroke-width="1" fill="none"/></svg>
          www.varneck-law-example.com
        </li>
      </ul>
      <address class="contact__address">
        Southern California,<br>
        4810 Harbor View Ave. #300<br>
        Seacliff Bay, CA 90000
      </address>
    </div>

    <div class="practice-band">Practice areas, Criminal Law, Civil Litigation/Personal Injury, Restraining</div>
  </section>

</body>
</html>
```